businesscard, flyer and membercard

--------------------------------------------------------------------------------------------------
design flyer :
- delivering format (jpg, pdf and original psd)
- there is a example how the flyers should look like
the text and logo should be the same as the exemple flyer, the creativity is yours.
- the design should have a back and front side.
File format : 15,0 cm x 21,2 cm
design membercard :
- there is example how the member-card should look like
the text and logo should be the same as the exemple membercard, the creativity is yours.
- the front side contains text and open space where for writing :
Naam ......
Dansstijlen ......
- the front side contains 12 circels horizontal at the line name at the end of the line "Salsa".
- the front side contains 12 circels horizontal at the line name at the end of the line "Bachata".
- the front side contains 12 circels horizontal at the line name at the end of the line "Kizomba".
- each horizontal line with circels contains a different kind of color/design.
- file format: 7,6 cm x 10,7 cm
Business card :
- there is example how the businesscard should look like
the text and logo should be the same as the exemple buisinesscard, the creativity is yours.
- the design should have a back a front side
File format : 8,7 cm x 5,7 cm

Target Market(s)

Dancing :Salsa, Bachata and Kizomba

Colors

Designer to choose colors to be used in the design.

Requirements
Must have
• same text as seen on the examples.
Nice to have
• see the examples as attachments
Should not have
• - REMOVE TEXT "KOV" from the design
• - REMOVE TEXT "Gratis Parkeren"

```html
<!DOCTYPE html>
<html lang="nl">
<head>
<meta charset="utf-8">
<title>Volta Dance Studio – Lidkaart en visitekaartje</title>
<link href="https://fonts.googleapis.com/css2?family=Raleway:wght@400;500&family=Montserrat:wght@600;700&display=swap" rel="stylesheet">
<style>
  :root{
    --board-top:#3a4246;
    --board-bottom:#1a1c1e;
    --card:#050505;
    --smoke:rgba(120,60,60,.22);
    --white:#ffffff;
    --muted:#d8d8d8;
    --red:#e3222b;
    --yellow:#f7ea1c; --salmon:#f07a62; --green:#33b34a; --pink:#e8175d;
    --cyan:#1cb5e8; --olive:#a7a33a; --purple:#6f2a78; --orange:#f26a2b;
    --amber:#f59a24; --navy:#1e3660; --brightred:#ed1c24;
  }
  *{margin:0;padding:0;box-sizing:border-box}
  html,body{width:1200px;height:1200px;overflow:hidden}
  body{
    position:relative;
    background:radial-gradient(ellipse at 50% 0%,var(--board-top),var(--board-bottom) 75%);
    font-family:"Raleway",sans-serif;color:var(--white);
  }
  .section-label{position:absolute;font-family:"Raleway",sans-serif;font-weight:500;font-size:34px;color:var(--white)}
  .section-label--member{left:46px;top:74px}
  .section-label--business{left:98px;top:608px}

  .card{position:absolute;background:var(--card);overflow:hidden;box-shadow:0 4px 14px rgba(0,0,0,.6)}
  .card--member{width:568px;height:403px;top:142px}
  .card--member-front{left:26px}
  .card--member-back{left:613px}
  .card--business{width:489px;height:321px;top:676px}
  .card--business-front{left:95px}
  .card--business-back{left:611px}
  .smoke{position:absolute;inset:0;
    background:radial-gradient(ellipse 60% 45% at 30% 45%,var(--smoke),transparent 70%),
               radial-gradient(ellipse 50% 40% at 75% 70%,var(--smoke),transparent 70%)}

  .abs{position:absolute}
  .center{text-align:center}
  .brand{font-family:"Raleway",sans-serif;font-weight:500;color:var(--white);letter-spacing:.12em;
    display:flex;align-items:center;justify-content:center;gap:8px}
  .brand-dot{display:inline-block;border-radius:50%;background:var(--red)}
  .studio{font-family:"Montserrat",sans-serif;font-weight:700;color:var(--white)}
  .tagline{font-size:5px;letter-spacing:.08em;color:var(--muted);font-style:italic}
  .dancer{background:linear-gradient(160deg,rgba(227,34,43,.55),rgba(227,34,43,.15));border-radius:40% 40% 30% 30%}

  .title{font-family:"Montserrat",sans-serif;font-weight:700;font-size:33px}
  .field{font-size:17px;color:var(--muted);white-space:nowrap}
  .field-line{display:inline-block;border-bottom:1px dashed var(--muted);vertical-align:middle;margin-left:6px}
  .dots{display:flex;gap:7.6px}
  .dot{width:26px;height:26px;border-radius:50%}
  .style-label{font-family:"Montserrat",sans-serif;font-weight:600;font-size:22px;letter-spacing:.04em}

  .style-word{position:absolute;font-family:"Montserrat",sans-serif;font-weight:700;white-space:nowrap;line-height:1}
  .style-sep{position:absolute;width:2px;background:var(--white)}
  .contact{display:flex;flex-direction:column}
  .contact-row{display:flex;align-items:center;white-space:nowrap}
  .contact-row svg{flex:none}
  .bracket{border-color:var(--white);border-style:solid;width:22px;height:20px}
</style>
</head>
<body>
  <div class="section-label section-label--member">Member Card</div>

  <!-- Member card front -->
  <section class="card card--member card--member-front">
    <div class="smoke" role="img" aria-label="Soft dark red smoke swirls"></div>
    <div class="abs dancer" style="left:18px;top:18px;width:72px;height:80px" role="img" aria-label="Red line drawing of a dancing couple"></div>
    <div class="abs dancer" style="left:479px;top:18px;width:72px;height:80px" role="img" aria-label="Red line drawing of a dancing couple"></div>
    <div class="abs brand" style="left:0;width:568px;top:30px;font-size:28px">VOLTA<span class="brand-dot" style="width:10px;height:10px"></span></div>
    <div class="abs center studio" style="left:0;width:568px;top:103px;font-size:13px">DANCE STUDIO</div>
    <div class="abs center tagline" style="left:0;width:568px;top:120px">MOVE WITH THE RHYTHM TOGETHER</div>
    <div class="abs center title" style="left:0;width:568px;top:133px">LID KAART</div>
    <div class="abs field" style="left:28px;top:186px">Naam :<span class="field-line" style="width:218px"></span></div>
    <div class="abs field" style="left:28px;top:214px">Dansstijlen :<span class="field-line" style="width:218px"></span></div>

    <div class="abs dots" style="left:29px;top:257px">
      <i class="dot" style="background:var(--yellow)"></i><i class="dot" style="background:var(--salmon)"></i><i class="dot" style="background:var(--green)"></i><i class="dot" style="background:var(--pink)"></i><i class="dot" style="background:var(--cyan)"></i><i class="dot" style="background:var(--olive)"></i><i class="dot" style="background:var(--brightred)"></i><i class="dot" style="background:var(--purple)"></i><i class="dot" style="background:var(--orange)"></i><i class="dot" style="background:var(--green)"></i><i class="dot" style="background:var(--amber)"></i><i class="dot" style="background:var(--navy)"></i>
    </div>
    <div class="abs style-label" style="left:442px;top:255px">Salsa</div>

    <div class="abs dots" style="left:29px;top:298px">
      <i class="dot" style="background:var(--navy)"></i><i class="dot" style="background:var(--amber)"></i><i class="dot" style="background:var(--green)"></i><i class="dot" style="background:var(--orange)"></i><i class="dot" style="background:var(--purple)"></i><i class="dot" style="background:var(--brightred)"></i><i class="dot" style="background:var(--olive)"></i><i class="dot" style="background:var(--cyan)"></i><i class="dot" style="background:var(--pink)"></i><i class="dot" style="background:var(--green)"></i><i class="dot" style="background:var(--salmon)"></i><i class="dot" style="background:var(--yellow)"></i>
    </div>
    <div class="abs style-label" style="left:441px;top:297px">Bachata</div>

    <div class="abs dots" style="left:29px;top:338px">
      <i class="dot" style="background:var(--brightred)"></i><i class="dot" style="background:var(--green)"></i><i class="dot" style="background:var(--purple)"></i><i class="dot" style="background:var(--orange)"></i><i class="dot" style="background:var(--yellow)"></i><i class="dot" style="background:var(--navy)"></i><i class="dot" style="background:var(--green)"></i><i class="dot" style="background:var(--cyan)"></i><i class="dot" style="background:var(--salmon)"></i><i class="dot" style="background:var(--olive)"></i><i class="dot" style="background:var(--pink)"></i><i class="dot" style="background:var(--amber)"></i>
    </div>
    <div class="abs style-label" style="left:441px;top:337px">Kizomba</div>
  </section>

  <!-- Member card back -->
  <section class="card card--member card--member-back">
    <div class="smoke" role="img" aria-label="Soft dark red smoke swirls"></div>
    <div class="abs dancer" style="left:420px;top:266px;width:135px;height:110px" role="img" aria-label="Red line drawing of a dancing couple"></div>
    <div class="abs brand" style="left:0;width:568px;top:44px;font-size:42px">VOLTA<span class="brand-dot" style="width:14px;height:14px"></span></div>
    <div class="abs center studio" style="left:0;width:568px;top:160px;font-size:22px">DANCE STUDIO</div>
    <div class="abs center tagline" style="left:0;width:568px;top:188px">MOVE WITH THE RHYTHM TOGETHER</div>
    <div class="style-word" style="left:41px;top:226px;font-size:30px">SALSA</div>
    <div class="style-word" style="left:186px;top:226px;font-size:30px">BACHATA</div>
    <div class="style-word" style="left:371px;top:226px;font-size:30px">KIZOMBA</div>
    <div class="abs contact" style="left:44px;top:271px;gap:5px;font-size:18px">
      <div class="contact-row" style="gap:6px">
        <svg width="24" height="16" viewBox="0 0 24 16"><path d="M2 6c0-3 20-3 20 0v2h-5V6H7v2H2z M6 9h12l3 6H3z" fill="var(--red)"/></svg>0612 480 735</div>
      <div class="contact-row" style="gap:6px">
        <svg width="24" height="16" viewBox="0 0 24 16"><rect x="1" y="2" width="22" height="13" fill="var(--red)"/><path d="M1 2l11 8 11-8" stroke="#050505" stroke-width="1.6" fill="none"/></svg>voltastudio@mailbox.nl</div>
      <div class="contact-row" style="gap:6px">
        <svg width="24" height="16" viewBox="0 0 24 16"><rect x="7" y="2" width="11" height="12" fill="var(--red)"/></svg>voltastudio@social.nl</div>
      <div class="contact-row" style="gap:6px">
        <svg width="24" height="18" viewBox="0 0 24 18"><path d="M12 17C7 11 6 9 6 6a6 6 0 0 1 12 0c0 3-1 5-6 11z" fill="var(--red)"/><circle cx="12" cy="6" r="2.2" fill="#050505"/></svg>Parkweg 22, 1234 AB Rivierstad</div>
    </div>
  </section>

  <div class="section-label section-label--business">Business Card</div>

  <!-- Business card front -->
  <section class="card card--business card--business-front">
    <div class="smoke" role="img" aria-label="Soft dark red smoke swirls"></div>
    <div class="abs brand" style="left:0;width:489px;top:36px;font-size:34px">VOLTA<span class="brand-dot" style="width:12px;height:12px"></span></div>
    <div class="abs center studio" style="left:0;width:489px;top:134px;font-size:17px">DANCE STUDIO</div>
    <div class="abs center tagline" style="left:0;width:489px;top:156px">MOVE WITH THE RHYTHM TOGETHER</div>
    <div class="abs contact" style="left:30px;top:188px;gap:6px;font-size:20px">
      <div class="contact-row" style="gap:8px">
        <svg width="18" height="18" viewBox="0 0 18 18"><circle cx="9" cy="5" r="4" fill="var(--white)"/><path d="M2 17c0-5 3-7 7-7s7 2 7 7z" fill="var(--white)"/></svg>Mira</div>
      <div class="contact-row" style="gap:8px">
        <svg width="18" height="14" viewBox="0 0 24 16"><path d="M2 6c0-3 20-3 20 0v2h-5V6H7v2H2z M6 9h12l3 6H3z" fill="var(--white)"/></svg>0612 480 735</div>
      <div class="contact-row" style="gap:8px">
        <svg width="18" height="12" viewBox="0 0 24 16"><rect x="1" y="2" width="22" height="13" fill="var(--white)"/><path d="M1 2l11 8 11-8" stroke="#050505" stroke-width="1.6" fill="none"/></svg>voltastudio@mailbox.nl</div>
      <div class="contact-row" style="gap:8px">
        <svg width="18" height="16" viewBox="0 0 18 18"><rect x="2" y="2" width="14" height="14" rx="2" fill="var(--white)"/></svg>voltastudio@social.nl</div>
    </div>
  </section>

  <!-- Business card back -->
  <section class="card card--business card--business-back">
    <div class="smoke" role="img" aria-label="Soft dark red smoke swirls"></div>
    <div class="abs brand" style="left:0;width:489px;top:34px;font-size:28px">VOLTA<span class="brand-dot" style="width:10px;height:10px"></span></div>
    <div class="abs center studio" style="left:0;width:489px;top:113px;font-size:15px">DANCE STUDIO</div>
    <div class="abs center tagline" style="left:0;width:489px;top:132px">MOVE WITH THE RHYTHM TOGETHER</div>
    <div class="abs bracket" style="left:25px;top:154px;border-width:2px 0 0 2px"></div>
    <div class="style-word" style="left:36px;top:166px;font-size:25px">SALSA</div>
    <div class="style-sep" style="left:144px;top:176px;height:11px"></div>
    <div class="style-word" style="left:161px;top:166px;font-size:25px">BACHATA</div>
    <div class="style-sep" style="left:308px;top:176px;height:11px"></div>
    <div class="style-word" style="left:322px;top:166px;font-size:25px">KIZOMBA</div>
    <div class="abs bracket" style="left:445px;top:176px;border-width:0 2px 2px 0"></div>
    <div class="abs center" style="left:0;width:489px;top:279px;font-size:20px;letter-spacing:.03em">Parkweg 22, 1234 AB Rivierstad</div>
  </section>
</body>
</html>
```